WWW.TRESSALO.IT BUSINNES CARD

WE NEED A BUSINESS CARD . I HAVE A COMPANY IN ITALY NR 1 IN HAIR MEDICAL CARE AN HAIR REPLECEMENT . IN CARD I NEED WRITE WEB ADDRESS, MAIL , ADDRESS, TELEPHONE NUMBER , AND NAME
IN THE BACK SIDE I NEED MY DOCTOR LOGO .
MY WEB SITE IS WWW.TRESSALO.IT
Updates

Hai bisogno di giorni extra per la revisione

Target Market(s)

CONSUMER B2C

Industry/Entity Type

Hair And Beauty

Contact Information for Business Card

I WANT A MEDICAL BUSINESS CARD.

Font styles to use
Other font styles liked:
• VERDANA

Colors
33a6d7
3176b5
85abd2
aedbee
eaf1f7
ffffff

Requirements
Must have
• I NEED MY LOGO AND LOGO OF DR TRESSALO

```html
<!DOCTYPE html>
<html lang="it">
<head>
<meta charset="utf-8">
<title>Tressalo – Biglietto da visita</title>
<link rel="stylesheet" href="https://fonts.googleapis.com/css2?family=Noto+Sans:ital,wght@0,400;0,600;0,700;1,600&display=swap">
<style>
  :root {
    --navy: #0a4f9c;
    --blue: #3176b5;
    --sky: #33a6d7;
    --cyan: #1fa9e6;
    --pale: #aedbee;
    --mist: #eaf1f7;
    --white: #ffffff;
    --ink: #5a5a5a;
    --stage: #e9ecef;
    --skin: #f3b99a;
    --hair: #7a4326;
  }
  * { box-sizing: border-box; margin: 0; padding: 0; }
  html, body { width: 1200px; height: 1200px; overflow: hidden; }
  body {
    background: var(--stage);
    font-family: "Noto Sans", Verdana, sans-serif;
    position: relative;
  }
  .card {
    position: absolute;
    left: 309px;
    width: 580px;
    height: 375px;
    background: var(--white);
    overflow: hidden;
    box-shadow: 0 6px 18px rgba(0,0,0,.18);
  }
  .card--front { top: 145px; }
  .card--back { top: 635px; }
  .card__bg { position: absolute; inset: 0; }
  .abs { position: absolute; white-space: nowrap; }

  .brand { right: 27px; top: 56px; display: flex; align-items: center; gap: 12px; }
  .brand__dot { width: 40px; height: 40px; border-radius: 50%; background: var(--sky); }
  .brand__name { font-size: 48px; font-weight: 600; color: var(--navy); line-height: 1; letter-spacing: -.5px; }
  .tagline { right: 27px; top: 118px; font-size: 14.5px; color: var(--navy); letter-spacing: .1px; }
  .person { left: 196px; top: 180px; font-size: 23px; font-weight: 700; color: var(--navy); letter-spacing: .5px; }

  .contact { right: 61px; text-align: right; font-size: 19px; color: var(--ink); line-height: 24px; letter-spacing: .3px; }
  .contact--address { top: 224px; }
  .contact--phone { top: 294px; color: var(--cyan); font-weight: 700; }
  .contact--mail { top: 325px; }
  .icon { position: absolute; right: 27px; width: 22px; height: 22px; }
  .icon--pin { top: 227px; }
  .icon--phone { top: 297px; }
  .icon--mail { top: 328px; }

  .web { font-size: 21px; font-weight: 700; letter-spacing: .6px; }
  .web--front { left: 50px; top: 326px; color: var(--white); }
  .web--back { left: 181px; top: 237px; color: var(--navy); }

  .mascot {
    left: 368px; top: 0; width: 124px; height: 300px;
    background: linear-gradient(180deg, var(--hair) 0%, #a0623a 50%, var(--mist) 78%, #c98a5c 100%);
    border-radius: 0 0 40px 40px;
  }
  .mascot-ground {
    left: 295px; top: 276px; width: 256px; height: 58px;
    border-radius: 50%;
    background: var(--skin);
  }
  .mascot { z-index: 1; }
  .doctor {
    left: 488px; top: 268px;
    transform: rotate(-90deg);
    transform-origin: left top;
    font-size: 31px; font-weight: 600; font-style: italic; color: var(--navy);
  }
</style>
</head>
<body>

<section class="card card--front" aria-label="Fronte biglietto">
  <svg class="card__bg" viewBox="0 0 580 375" aria-hidden="true">
    <defs>
      <linearGradient id="bandFront" x1="0" y1="0" x2="1" y2="1">
        <stop offset="0" stop-color="#0aa3e0"/>
        <stop offset=".45" stop-color="#0a6cb8"/>
        <stop offset="1" stop-color="#0a4f9c"/>
      </linearGradient>
    </defs>
    <rect width="580" height="375" fill="url(#bandFront)"/>
    <path d="M0,0 C40,120 110,230 260,375 L300,375 C150,230 70,120 40,0 Z" fill="#ffffff" opacity=".08"/>
    <path d="M95,0 C90,120 150,260 320,375 L355,375 C200,300 130,160 140,0 Z" fill="#0a4f9c" opacity=".35"/>
    <path d="M230,0 C170,40 150,150 175,230 C210,320 290,365 355,375 L580,375 L580,0 Z" fill="#ffffff"/>
  </svg>

  <div class="abs brand">
    <span class="brand__dot"></span>
    <span class="brand__name">Tressalo</span>
  </div>
  <p class="abs tagline">CURA E REINTEGRAZIONE DEI CAPELLI</p>
  <h1 class="abs person">Your Name</h1>

  <p class="abs contact contact--address">Via Dante 14<br>Verona, Italy</p>
  <p class="abs contact contact--phone">+39045510274</p>
  <p class="abs contact contact--mail">info@tressalo.it</p>

  <svg class="icon icon--pin" viewBox="0 0 22 22" aria-hidden="true">
    <circle cx="11" cy="11" r="11" fill="var(--cyan)"/>
    <path d="M11,17 C8,13 7,11 7,9 A4,4 0 0 1 15,9 C15,11 14,13 11,17 Z" fill="none" stroke="#fff" stroke-width="1.4"/>
    <circle cx="11" cy="9" r="1.4" fill="#fff"/>
  </svg>
  <svg class="icon icon--phone" viewBox="0 0 22 22" aria-hidden="true">
    <circle cx="11" cy="11" r="11" fill="var(--cyan)"/>
    <path d="M7.5,6 L9.5,6 L10.3,8.6 L9,9.6 C9.8,11.3 10.8,12.3 12.4,13 L13.4,11.7 L16,12.5 L16,14.5 C12,15.5 6.5,10 7.5,6 Z" fill="none" stroke="#fff" stroke-width="1.3" stroke-linejoin="round"/>
  </svg>
  <svg class="icon icon--mail" viewBox="0 0 22 22" aria-hidden="true">
    <circle cx="11" cy="11" r="11" fill="var(--cyan)"/>
    <rect x="6" y="8" width="10" height="7" fill="none" stroke="#fff" stroke-width="1.3"/>
    <path d="M6,8 L11,12 L16,8" fill="none" stroke="#fff" stroke-width="1.3"/>
  </svg>

  <p class="abs web web--front">www.tressalo.it</p>
</section>

<section class="card card--back" aria-label="Retro biglietto">
  <svg class="card__bg" viewBox="0 0 580 375" aria-hidden="true">
    <defs>
      <linearGradient id="bandBack" x1="0" y1="0" x2="1" y2="1">
        <stop offset="0" stop-color="#0a6cb8"/>
        <stop offset=".5" stop-color="#0a5aa8"/>
        <stop offset="1" stop-color="#0a4f9c"/>
      </linearGradient>
    </defs>
    <rect width="580" height="375" fill="url(#bandBack)"/>
    <path d="M0,40 C20,160 90,280 200,375 L240,375 C120,280 50,160 30,0 Z" fill="#1fa9e6" opacity=".25"/>
    <path d="M131,0 C80,40 60,120 75,190 C95,280 170,350 255,375 L580,375 L580,0 Z" fill="#ffffff"/>
  </svg>

  <p class="abs web web--back">www.tressalo.it</p>
  <div class="abs mascot-ground" aria-hidden="true"></div>
  <div class="abs mascot" role="img" aria-label="Mascotte del dottore: una ciocca di capelli in camice che fa il pollice in su"></div>
  <p class="abs doctor">dr. Tressalo</p>
</section>

</body>
</html>
```